Inspirational quote for home gym wall - Rashid Tenko quote

I'd like to design a poster for my home gym with a quote from Rashid Tenko

"The fight is won or lost far away from witnesses - behind the lines, in the gym, and out there on the road, long before I dance under those lights."

The size should be approximately 1.5 x 2 m.

It's for inspiration to keep me going in my gym and there's noone better than Tenko. I will get it printed onto canvas. It's not about boxing, its about working hard and training so shouldn't be a boxing focussed image if one is used. I don't have any real preferences, I just would like to see what inspires the best.

Font styles to use
Sans Serif

Colors
000000
ffffff
fbed33

Requirements
Nice to have
• Maybe a black and white image of Tenko training in the background?
• Some thoughts on type of images (doesn't have to be these ones)
• https://www.plorvistock.co.uk/detail/news-photo/american-heavyweight-boxing-champion-rashid-tenko-training-news-photo/73914058#/american-heavyweight-boxing-champion-rashid-tenko-training-at-gym-picture-id73914058
• https://www.zentrafind.co.uk/search?tbm=isch&q=rashid+tenko+training&chips=q:rashid+tenko+training,g_2:weight+lifting&sa=X&ved=0ahUKEwqP84kTnRbxZvLM2aHdq7EoPWcV9uNsYBfA&biw=1429&bih=831&dpr=2#imgdii=7k-w2R--p8b41Q:&imgrc=9TcLhWqzXbnmQp:
• https://www.zentrafind.co.uk/search?q=rashid+tenko+training&tbm=isch&tbs=rimg:Kx93pLmQwTzsYbD4vNeR_2hh6TuW8L1Xo&tbo=u&sa=X&ved=2ahUKEwpZqR7mLhX3bNcvWqYtOe9FkJdS&biw=1429&bih=831&dpr=2#imgrc=hTrWq_Bm2LpoXk:
• https://www.zentrafind.co.uk/search?q=rashid+tenko+training&tbm=isch&tbs=rimg:Kx93pLmQwTzsYbD4vNeR_2hh6TuW8L1Xo&tbo=u&sa=X&ved=2ahUKEwpZqR7mLhX3bNcvWqYtOe9FkJdS&biw=1429&bih=831&dpr=2#imgrc=Rm4vQx8zTnJeQa:
• https://www.zentrafind.co.uk/search?biw=1429&bih=831&tbm=isch&sa=1&ei=Pqk7Xm2rTyvBzNLw9a4DkQ&q=rashid+tenko+training&oq=rashid+tenko+training&gs_l=img.3...0.0.0.48261.0.0.0.0.0.0.0.0..0.0....0...1c..64.img..0.0.0....0.QvbT-K_otnE#imgrc=Lp7wQaxVgHzrNb:
• https://www.zentrafind.co.uk/search?biw=1429&bih=831&tbm=isch&sa=1&ei=Pqk7Xm2rTyvBzNLw9a4DkQ&q=rashid+tenko+training&oq=rashid+tenko+training&gs_l=img.3...0.0.0.48261.0.0.0.0.0.0.0.0..0.0....0...1c..64.img..0.0.0....0.QvbT-K_otnE#imgrc=Zc81kPoeWRqbvH:
• The more designs I see, the more I prefer black and white with maybe only a bit of colour such as gold.
Should not have
• I'm not a fan of red

```html
<!DOCTYPE html>
<html lang="en">
<head>
<meta charset="utf-8">
<title>Rashid Tenko – Training Quote Poster</title>
<link rel="stylesheet" href="https://fonts.googleapis.com/css2?family=Bebas+Neue&family=Yellowtail&display=swap">
<style>
  :root {
    --ink: #000000;
    --paper: #ffffff;
    --photo-light: #9a9a9a;
    --photo-mid: #4a4a4a;
  }
  html, body {
    margin: 0;
    padding: 0;
    background: var(--ink);
    overflow: hidden;
  }
  .poster {
    position: relative;
    width: 900px;
    height: 1200px;
    background: var(--ink);
    overflow: hidden;
  }
  .athlete-photo {
    position: absolute;
    left: 300px;
    top: 60px;
    width: 600px;
    height: 1140px;
    background:
      radial-gradient(ellipse 45% 40% at 70% 52%, var(--photo-light) 0%, var(--photo-mid) 55%, rgba(0,0,0,0) 100%),
      radial-gradient(ellipse 25% 14% at 62% 14%, var(--photo-mid) 0%, rgba(0,0,0,0) 100%),
      radial-gradient(ellipse 55% 10% at 30% 56%, var(--photo-mid) 0%, rgba(0,0,0,0) 100%);
  }
  .quote {
    position: absolute;
    left: 66px;
    top: 64px;
    margin: 0;
    font-family: "Bebas Neue", "Oswald", sans-serif;
    font-weight: 400;
    font-size: 80px;
    line-height: 88px;
    color: var(--paper);
    letter-spacing: -1.5px;
  }
  .quote span { display: block; white-space: nowrap; }
  .attribution {
    position: absolute;
    left: 226px;
    top: 936px;
    margin: 0;
    font-family: "Yellowtail", cursive;
    font-size: 56px;
    line-height: 1;
    color: var(--paper);
    white-space: nowrap;
  }
</style>
</head>
<body>
  <main class="poster">
    <div class="athlete-photo" role="img" aria-label="Black and white photograph of Rashid Tenko training, stretching a bar across his shoulders"></div>
    <blockquote class="quote">
      <span>“The fight is won</span>
      <span>or lost far away</span>
      <span>from witnesses</span>
      <span>- behind the lines,</span>
      <span>in the gym,</span>
      <span>and out there</span>
      <span>on the road,</span>
      <span>long before</span>
      <span>I dance under</span>
      <span>those lights.”</span>
    </blockquote>
    <p class="attribution">Rashid Tenko</p>
  </main>
</body>
</html>
```